Law Firm from Estonia. E-S-T-O-N-I-A. Country of nice people and bad skiing weather

Just in case there is still a misunderstanding here - this is a project for the Letterhead, Logo and Business Card (i.e THREE designs). Due to some odd reason the system does not always show Logo and Business Card part - we have written an e-mail to the ArtHive support on that.

Our current business name is Varendi & Lust by two owners.

We want turquoise blue as our corporate colour – against black and white background. As per logo and letterhead design – we would like it to be simple, modern and elegant.

We would like our corporate identity to express the following: best, vanguard, trustworthiness. Our logo must be:
-Classy and precious
-Simple, clean and elegant
-Timeless
-Trustworthy and strong

You should be heading for something LETTERED (we're legal), SIMPLE (we make other people's problems simple), STRAIGHTFORWARD, CORPORATE and CONFIDENT.

1. The Logo shall consist of two main parts: The company name and the symbol.
-The Brand Name is: Varendi & Lust
-The Symbol must be easy to recognize and clear.
Please suggest 3 symbols.
The name and the symbol must be usable together and separately, in colour (blue-green) and black&white.

Once The Logo has been set, please develop a stationary with the following items:
-Business Card
-Letterhead A4

Suggest 3 of each.

We are looking forward to your designs.
Updates

Dear all, As per light blue colour - could you please use BlueGreen palette (i.e turquoise, aquamarine, cyan blue, sea green etc) - i.e blue should contain a little bit of green. The colour palette provided here does not contain the right tone - the green blue is too green. Our blue should be bluer, but still contain a hint of green. Like, for example, Silkenbay products. Thank you!

Dear all, I do not know if you can see your colleagues' designs participating in the same contest, but they look alike as if you are using the same template. Therefore may we suggest that you do not use this horizontal S-wave and do something more creative. Moreover, it's about the LETTER of the law and about being straight - there is nothing in Law that is about waves. Please do NOT use waves! Our logo should be STRAIGHT and SOLID, but ELEGANT. Like Orvée. If you use our initials for logo, you may use different fonts. Just V&L is not appealing, we could create it ourselves in TextPad. Perhaps putting a full stop at the end of the initials might be interesting. Or, for example, have a look at Dawnfield Computing logo, forming an interesting square from the letters. As per colours - the palette here in ArtHive is very limited and all the colours look dirty. We would like our colours to be bright and clean. May we also suggest that you use colour gradient in some of your designs. We do not insist, but it might make the simple design (that we want) a bit more interesting. Kind regards Maret

Dear all, One of our partners has just suggested the following: The Law Firm's line is like the surgical incision: quick, clean and sharp. We hope it inspires you. Regards Maret

Hello everybody Nobody has ever done it yet, but as a combination of M and K you could use two triangles - if you connect M's legs and turn it clockwise to make it look like K I have unloaded some pictures that just came to my mind. Could you suggest something like this (too) please? Thank you

Dear all, Since your perception of turquoise might be different from ours, please find below a link with the exact colour we want. http://www.tintsample.example/colors/34DDDD OUR LOGO SHOULD BE MONOCHROME - the only colours that are allowed are turquoise (you may use hues), black and white. Please do NOT suggest green & blue, blue & red, red & orange etc. Regards Maret

Reason: One day to the deadline and we are not happy with the results yet. We hope this little extension helps. Regards Maret

Target Market(s)

Our clients are:
- mid- to large-sized companies
- managed by our agemates (let us say 35 and over),
- who are well educated middle-class males, married with children
- western languages speaking (English, Estonian, Scandinavian)

Industry/Entity Type

Business

Font styles to use
Sans Serif
Script

Colors
ecf7f6
ecf7f5
86cfc6
34b8a4
00a98f
33a6d7

Requirements
Should not have
• The design should not use old-style fonts
The design should not use serif fonts
Please do not use inaccurate informal fonts either
Please do not include common stamps of Themis (balance, sword, hammer etc)
Please do not use waves

```html
<!DOCTYPE html>
<html lang="en">
<head>
<meta charset="utf-8">
<title>Varendi &amp; Lust — Letterhead</title>
<link href="https://fonts.googleapis.com/css2?family=Josefin+Sans:wght@400;600&display=swap" rel="stylesheet">
<style>
  :root {
    --paper: #ffffff;
    --ink: #1a1a1a;
    --turquoise: #34b8a4;
    --fold: #bfbfbf;
  }
  * { margin: 0; padding: 0; box-sizing: border-box; }
  html, body { width: 849px; height: 1200px; overflow: hidden; background: var(--paper); }
  .letterhead {
    position: relative;
    width: 849px;
    height: 1200px;
    background: var(--paper);
    font-family: "Josefin Sans", sans-serif;
    color: var(--ink);
  }
  .brand {
    position: absolute;
    top: 56px;
    left: 0;
    width: 100%;
    text-align: center;
    line-height: 1;
  }
  .brand-lockup {
    display: inline-flex;
    align-items: center;
    gap: 12px;
  }
  .brand-symbol {
    width: 14px;
    height: 14px;
    background: var(--turquoise);
  }
  .brand-name {
    font-weight: 600;
    font-size: 20px;
    letter-spacing: 4px;
    color: var(--ink);
  }
  .brand-tagline {
    margin-top: 14px;
    font-size: 10px;
    letter-spacing: 0.8px;
    color: var(--turquoise);
  }
  .fold-mark {
    position: absolute;
    top: 376px;
    left: 0;
    width: 16px;
    height: 1px;
    background: var(--fold);
  }
  .contact {
    position: absolute;
    left: 0;
    width: 100%;
    text-align: center;
    font-size: 9px;
    letter-spacing: 1px;
    line-height: 1;
  }
  .contact-phones { top: 1136px; font-weight: 600; word-spacing: 3px; }
  .contact-phones .gap { display: inline-block; width: 14px; }
  .contact-address {
    top: 1147px;
    display: flex;
    align-items: center;
    gap: 10px;
    padding: 0 52px;
    color: var(--turquoise);
    font-size: 8px;
    letter-spacing: 0.6px;
  }
  .contact-address .rule { flex: 1; height: 1px; background: var(--turquoise); }
  .contact-web { top: 1160px; font-weight: 600; }
</style>
</head>
<body>
  <main class="letterhead">
    <header class="brand">
      <div class="brand-lockup">
        <span class="brand-symbol"></span>
        <span class="brand-name">VARENDI &amp; LUST</span>
      </div>
      <div class="brand-tagline">Solicitors at Law</div>
    </header>

    <div class="fold-mark"></div>

    <footer>
      <div class="contact contact-phones">TEL: +372 555 0148<span class="gap"></span>FAX: +372 555 0149</div>
      <div class="contact contact-address">
        <span class="rule"></span>
        <span>Law Firm Varendi &amp; Lust &nbsp; Kesklinna tn 12, 10111 Tallinn, Estonia</span>
        <span class="rule"></span>
      </div>
      <div class="contact contact-web">WWW.VARENDILUST.EE</div>
    </footer>
  </main>
</body>
</html>
```